Meridian Callware business card design

I would like to see some designs for a business card for Meridian Callware. I would like the business card to be double sided. It will need to have a similar colour / look and feel to our website www.meridiancallware.com.au I have also attached our latest flyer. Final designs to be handed over in Photoshop format so that I can edit the business card when needed please.

Industry/Entity Type

Business

Contact Information for Business Card

Kelvin Ashworth
sales@meridiancallware.com.au
Business Development Manager
ph: (08) 6517 2984
www.meridiancallware.com.au

Font styles to use
Serif
Sans Serif

Requirements
Must have
• If you could please utilise our colour scheme as seen on our website and the attached flyer.
• I would also like the final design to be in a Photoshop format so that I can edit it when needed please.

```html
<!DOCTYPE html>
<html lang="en">
<head>
<meta charset="utf-8">
<title>Meridian Callware – Business Card</title>
<link rel="stylesheet" href="https://fonts.googleapis.com/css2?family=Montserrat:wght@600&family=Source+Sans+3:wght@400;600&display=swap">
<style>
  :root {
    --page-bg: #e9e9eb;
    --card-dark: #1f2022;
    --card-blue: #2b8bd0;
    --brand-blue: #2a8fd6;
    --text-light: #f2f2f2;
    --text-muted: #d6d6d6;
    --white: #ffffff;
  }
  * { margin: 0; padding: 0; box-sizing: border-box; }
  html, body {
    width: 1200px; height: 844px; overflow: hidden;
    background: var(--page-bg);
  }
  .canvas {
    position: relative; width: 1200px; height: 844px;
    display: flex; align-items: center; justify-content: center; gap: 60px;
  }
  .card {
    width: 490px; height: 290px; border-radius: 4px;
    box-shadow: 0 6px 18px rgba(0,0,0,0.18);
    position: relative;
  }
  .card-back { background: var(--card-dark); }
  .card-front {
    background: var(--card-blue);
    display: flex; align-items: center; justify-content: center;
  }
  .wordmark {
    font-family: "Montserrat", sans-serif; font-weight: 600;
    letter-spacing: -0.5px; white-space: nowrap;
  }
  .card-back .wordmark {
    position: absolute; left: 50%; top: 62px; transform: translateX(-50%);
    font-size: 34px; color: var(--text-light);
  }
  .card-front .wordmark { font-size: 40px; color: var(--white); }
  .contact {
    position: absolute; left: 0; right: 0; top: 130px;
    text-align: center; font-family: "Source Sans 3", sans-serif;
    color: var(--text-muted); font-size: 15px; line-height: 1.3;
  }
  .contact-name { color: var(--brand-blue); font-weight: 600; font-size: 17px; }
  .contact-role { margin-bottom: 16px; }
  .contact-line { display: flex; align-items: center; justify-content: center; gap: 6px; }
  .contact-line.gap { margin-bottom: 10px; }
  .icon { width: 12px; height: 12px; fill: var(--brand-blue); flex: none; }
</style>
</head>
<body>
<main class="canvas">
  <section class="card card-back">
    <div class="wordmark">Meridian Callware</div>
    <div class="contact">
      <div class="contact-name">Kelvin Ashworth</div>
      <div class="contact-role">Business Development Manager</div>
      <div class="contact-line gap">
        <svg class="icon" viewBox="0 0 24 24" aria-hidden="true"><path d="M6.6 10.8a15 15 0 0 0 6.6 6.6l2.2-2.2c.3-.3.7-.4 1-.2 1.1.4 2.3.6 3.6.6.6 0 1 .4 1 1V20c0 .6-.4 1-1 1A17 17 0 0 1 3 4c0-.6.4-1 1-1h3.5c.6 0 1 .4 1 1 0 1.3.2 2.5.6 3.6.1.3 0 .7-.2 1z"/></svg>
        <span>(08) 6517 2984</span>
      </div>
      <div class="contact-line">
        <svg class="icon" viewBox="0 0 24 24" aria-hidden="true"><path d="M2 5h20v14H2z M2 5l10 8 10-8" /><path d="M3 6l9 7 9-7" fill="#1f2022"/></svg>
        <span>sales@meridiancallware.com.au</span>
      </div>
      <div class="contact-line">
        <svg class="icon" viewBox="0 0 24 24" aria-hidden="true"><circle cx="12" cy="12" r="10"/><path d="M2 12h20M12 2c3 3 3 17 0 20M12 2c-3 3-3 17 0 20" stroke="#1f2022" stroke-width="1.6" fill="none"/></svg>
        <span>www.meridiancallware.com.au</span>
      </div>
    </div>
  </section>
  <section class="card card-front">
    <div class="wordmark">Meridian Callware</div>
  </section>
</main>
</body>
</html>
```